Copper Ridge Resort & Marina - Boat Slips, Cabin Rentals, Floating Vacation Homes, & More

We need an 8'H x 16'W billboard for our Resort & marina, www.copperridgeresort.example. We'd like it to include: Lakefront Cabin Rentals, Floating Vacation Homes, and New Slips Summer 2022. We'd like it to be simple using the colors on our logo, similar to our business cards, and have our logo on it large. Maybe an arrow on the bottom pointing left that says 3 miles, possibly our website and phone number.

Target Market(s)

Lake People, Boaters

Industry/Entity Type

Resort & Marina (Recreation/Hospitality)

Font styles to use
Sans Serif
Other font styles liked:
• Simple/modern

Colors
0054AA
0677BA
7BADD7
CADEEF
E8F1F8
FFC000
F8CF3A
FAE287
FDF2CF
FEFAEE
F0912C
F2A743
F7CA91
FBE8D2
FDF5EE

Requirements
Must have
• Logo, Cabin Rentals, Floating Vacation Homes, New Slips Summer 2022
Nice to have
• An additional banner hanging from the bottom with an orange (or blue, colors from our logo) arrow pointing left, with white text saying: 3 miles 555-214-0867 www.copperridgeresort.example
Should not have
• Shouldn't be too busy

```html
<!DOCTYPE html>
<html lang="en">
<head>
<meta charset="utf-8">
<title>Copper Ridge Resort &amp; Marina Billboard</title>
<link rel="stylesheet" href="https://fonts.googleapis.com/css2?family=Tinos:wght@400;700&display=swap">
<style>
  :root {
    --navy: #154c82;
    --panel: #e1e4ee;
    --stripe: #f5a623;
    --arrow: #e8523a;
    --white: #ffffff;
    --edge: #333333;
  }
  html, body {
    margin: 0;
    padding: 0;
    width: 1200px;
    height: 1200px;
    overflow: hidden;
    background: var(--white);
  }
  .billboard {
    display: block;
    width: 1200px;
    height: 1200px;
  }
  .serif { font-family: "Tinos", "Times New Roman", serif; }
  .brand-name { fill: var(--navy); font-size: 62px; font-weight: 400; }
  .brand-sub { fill: var(--navy); font-size: 26px; font-weight: 400; }
  .feature { fill: var(--navy); font-size: 41px; font-weight: 400; }
  .distance { fill: var(--white); font-size: 122px; font-weight: 700; }
  .call { fill: var(--white); font-size: 60px; font-weight: 400; }
  .website { fill: var(--white); font-size: 35px; font-weight: 400; }
</style>
</head>
<body>
<svg class="billboard" viewBox="0 0 1200 1200" xmlns="http://www.w3.org/2000/svg">
  <defs>
    <linearGradient id="bullet-fill" x1="0" y1="0" x2="0" y2="1">
      <stop offset="0" stop-color="#f7c133"/>
      <stop offset="1" stop-color="#e8523a"/>
    </linearGradient>
  </defs>

  <!-- main board -->
  <g class="main-board">
    <rect x="70" y="232" width="1076" height="314" fill="var(--panel)" stroke="var(--edge)" stroke-width="1"/>
    <rect class="band-top" x="70" y="232" width="1076" height="42" fill="var(--navy)"/>
    <rect class="stripe-top" x="70" y="284" width="1076" height="4" fill="var(--stripe)"/>
    <rect class="stripe-bottom" x="70" y="485" width="1076" height="4" fill="var(--stripe)"/>
    <rect class="band-bottom" x="70" y="500" width="1076" height="46" fill="var(--navy)"/>

    <g class="brand">
      <circle cx="344" cy="350" r="30" fill="var(--stripe)"/>
      <text class="brand-name serif" x="104" y="436" textLength="480" lengthAdjust="spacingAndGlyphs">COPPER RIDGE</text>
      <text class="brand-sub serif" x="194" y="468" textLength="318" lengthAdjust="spacing">RESORT &amp; MARINA</text>
    </g>

    <g class="features">
      <circle cx="660" cy="338" r="9" fill="url(#bullet-fill)"/>
      <text class="feature serif" x="682" y="352">Lakefront Cabin Rentals</text>
      <circle cx="660" cy="386" r="9" fill="url(#bullet-fill)"/>
      <text class="feature serif" x="682" y="401">Floating Vacation Homes</text>
      <circle cx="660" cy="436" r="9" fill="url(#bullet-fill)"/>
      <text class="feature serif" x="682" y="450">New Slips Summer 2022</text>
    </g>
  </g>

  <!-- direction banner -->
  <g class="direction-banner">
    <rect x="70" y="590" width="1076" height="158" fill="var(--panel)" stroke="var(--edge)" stroke-width="1"/>
    <polygon class="arrow" points="72,669 194,590 1146,590 1062,669 1146,748 194,748" fill="var(--arrow)"/>
    <text class="distance serif" x="182" y="708" textLength="368" lengthAdjust="spacingAndGlyphs">3 miles</text>
    <text class="call serif" x="576" y="672" textLength="464" lengthAdjust="spacingAndGlyphs">Call: 555-214-0867</text>
    <text class="website serif" x="580" y="716" textLength="458" lengthAdjust="spacingAndGlyphs">www.copperridgeresort.example</text>
  </g>
</svg>
</body>
</html>
```